The Nine Gates for Tablet Reliance - Contemporary Book Cover Design

The Nine Gates for Tablet Reliance was published in March 2019 and is available on Brimora and other platforms now. However, I am not happy with the cover.  It's a good design in some ways - I thought it would stand out and be easily recognizable. But I don't really like the color scheme and feel that a self-help book should probably use some lighter colors and that the red is too strident. The color scheme carries over into other marketing materials like the website, social media, etc. and I don't like the red and black scheme for these purposes.
It's not essential that the cover contain an endorsement like the current one but it could. Here are some endorsements:
“A must-read for anyone who is addicted to or thinks they may have a problem with digital technology. This eloquent work will also be useful to academics and clinicians exploring potential solutions. The author recognizes the similarities between smartphone addiction and other addictions, and logically applies one of the most effective known solutions for addiction - The Nine Gates.”
-- Dale Wickersham: Noted Interventionist, Keynote Speaker and Addiction Visionary
“If you suffer from digital addiction, I strongly encourage you to use this book as your road map to get you back to the real world.”
-- Thomas Quillard, Founder of Online Channel Monitor.
The back cover would have the new design / color scheme, but can have similar text, bio, author image, etc. Or we could include the endorsements there and shorten the other text.
As for the cover it could be stylized, or an image, a partial image, or whatever. I am open to suggestions. Think about what would be inviting for a person searching for help with moderating their smartphone use.
Let's add a subtitle as well "An Inner Journey to Balanced Tablet Habits"
Here is a link to the book:
https://www.brimora.example/Nine-Gates-Tablet-Reliance/dp/4086213590

Target Market(s)
General, since this issue affects almost everyone.
Colors
Designer to choose colors to be used in the design.
Look and feel

```html
<!DOCTYPE html>
<html lang="en">
<head>
<meta charset="utf-8">
<title>The Nine Gates for Tablet Reliance — Caleb Moren</title>
<link rel="stylesheet" href="https://fonts.googleapis.com/css2?family=Bebas+Neue&display=swap">
<style>
  :root {
    --sky: #8ec6cf;
    --screen: #fffde6;
    --white: #ffffff;
    --ink: #1d1d1b;
    --orange: #f7953b;
    --green: #8cc540;
    --steel-blue: #93c6d2;
  }
  html, body {
    margin: 0;
    padding: 0;
    width: 800px;
    height: 1200px;
    overflow: hidden;
    background: var(--sky);
  }
  .cover {
    display: block;
    width: 800px;
    height: 1200px;
  }
  .cover-text {
    font-family: "Bebas Neue", "Oswald", sans-serif;
  }
  .author { fill: var(--ink); }
  .subtitle { fill: var(--ink); }
  .title-small--orange { fill: var(--orange); }
  .title-small--green { fill: var(--green); }
  .title-word--green { fill: var(--green); }
  .title-word--blue { fill: var(--steel-blue); }
  .title-word--ink { fill: var(--ink); }
  .title-word--orange { fill: var(--orange); }
</style>
</head>
<body>
<svg class="cover" viewBox="0 0 800 1200" xmlns="http://www.w3.org/2000/svg">
  <title>The Nine Gates for Tablet Reliance: An Inner Journey to Balanced Tablet Habits, by Caleb Moren</title>

  <rect class="device-body" x="0" y="0" width="800" height="1200" fill="var(--sky)"/>
  <rect class="device-speaker" x="360" y="50" width="80" height="14" rx="7" fill="var(--white)"/>
  <rect class="device-screen" x="50" y="100" width="698" height="954" fill="var(--screen)"/>

  <g class="device-home-button">
    <circle cx="400" cy="1112" r="42" fill="var(--white)"/>
    <rect x="383" y="1095" width="34" height="34" rx="11" fill="var(--sky)"/>
    <rect x="391" y="1103" width="18" height="18" rx="5" fill="var(--white)"/>
  </g>

  <g class="cover-text author" font-size="88">
    <text x="86" y="186" textLength="284" lengthAdjust="spacing">CALEB</text>
    <text x="440" y="186" textLength="276" lengthAdjust="spacing">MOREN</text>
  </g>

  <text class="cover-text subtitle" x="88" y="250" font-size="30" textLength="626" lengthAdjust="spacing">AN INNER JOURNEY TO BALANCED TABLET HABITS</text>

  <g class="cover-text title">
    <text class="title-small--orange" x="88" y="322" font-size="46" textLength="66" lengthAdjust="spacing">THE</text>
    <text class="title-word--green" x="86" y="474" font-size="190" textLength="628" lengthAdjust="spacing">NINE</text>
    <text class="title-word--blue" x="90" y="686" font-size="257" textLength="620" lengthAdjust="spacing">GATES</text>
    <text class="title-small--green" x="88" y="736" font-size="46" textLength="64" lengthAdjust="spacing">FOR</text>
    <text class="title-word--ink" x="86" y="852" font-size="131" textLength="628" lengthAdjust="spacing">TABLET</text>
    <text class="title-word--orange" x="88" y="1010" font-size="168" textLength="624" lengthAdjust="spacing">RELIANCE</text>
  </g>
</svg>
</body>
</html>
```